Castellan fine stockings - sexy cardboard box design needed!

We need a packaging design for a new online company based in Sydney called 'Castellan Stockings'. We will be selling sexy stockings to our customers by Italian designers. We mainly feature lace stockings, an example of which, can be seen here:
http://www.brunettapiovesi.example/italy-FASHION-WINTER

The design should be a cardboard pull out box, black in colour with the logo on the cover. We are looking for the logo to communicate sophistication and sexiness.

Examples of cardboard box shapes we would like are:
http://www.tradekornet.example/product-gs/836201947/High_quality_drawer_paper_box.html

http://www.tradekornet.example/product-gs/593174602/Cardboard_drawer_box.html

29 December:
I submitted a note when I extended the deadline, but cannot see it, so will write here for clarification. It has been difficult to choose the best design as the designs submitted were of such high quality. I want to have some people judge the designs, but because of the Christmas Season I have extended the deadline so that this can be done. Thanks.

Target Market(s)

The working professional woman.

Industry/Entity Type

Fashion

Requirements
Must have
• The words "Castellan Stockings" on the cover of the box.

The box should be a sliding drawer.

The box size should be: (22*15*2.5cm).

Washing instructions and recycling logos on the back of the box. See example of uploaded file.

Nice to have
• It would be nice to have the background of the box a dark colour, maybe charcoal? But we are open to all ideas.
Should not have
• A stock photo on cover of box.

```html
<!DOCTYPE html>
<html lang="en">
<head>
<meta charset="utf-8">
<title>Castellan Stockings – Box Cover Designs</title>
<link rel="stylesheet" href="https://fonts.googleapis.com/css2?family=Questrial&display=swap">
<style>
  :root {
    --page-bg: #ffffff;
    --charcoal: #25282b;
    --charcoal-pattern-deep: #2e3134;
    --charcoal-pattern-light: #45484b;
    --charcoal-swoosh: #6f7174;
    --cocoa: #6b3a22;
    --cocoa-pattern-deep: #8a5224;
    --cocoa-pattern-light: #c0843e;
    --cocoa-swoosh: #cf9a4f;
    --logo-ink: #f2f0ec;
  }

  * { margin: 0; padding: 0; box-sizing: border-box; }

  html, body {
    width: 1200px;
    height: 900px;
    overflow: hidden;
    background: var(--page-bg);
  }

  .canvas {
    position: relative;
    width: 1200px;
    height: 900px;
  }

  .cover {
    position: absolute;
    top: 216px;
    width: 320px;
    height: 468px;
    overflow: hidden;
  }

  .cover--charcoal { left: 84px; background: var(--charcoal); }
  .cover--cocoa { left: 488px; background: var(--cocoa); }

  .cover__art {
    position: absolute;
    inset: 0;
    width: 100%;
    height: 100%;
  }

  .cover--charcoal .pattern-stop-a { stop-color: var(--charcoal-pattern-light); }
  .cover--charcoal .pattern-stop-b { stop-color: var(--charcoal-pattern-deep); }
  .cover--charcoal .swoosh { fill: var(--charcoal-swoosh); }

  .cover--cocoa .pattern-stop-a { stop-color: var(--cocoa-pattern-light); }
  .cover--cocoa .pattern-stop-b { stop-color: var(--cocoa-pattern-deep); }
  .cover--cocoa .swoosh { fill: var(--cocoa-swoosh); }

  .brand {
    position: absolute;
    left: 104px;
    right: 10px;
    top: 376px;
    text-align: center;
    color: var(--logo-ink);
    font-family: "Questrial", "Century Gothic", sans-serif;
    font-weight: 400;
    line-height: 1;
  }

  .brand__name {
    display: block;
    font-size: 29px;
    letter-spacing: 0.5px;
  }

  .brand__line {
    display: block;
    margin-top: 6px;
    font-size: 8px;
    letter-spacing: 4px;
    padding-left: 4px;
  }
</style>
</head>
<body>
<main class="canvas">

  <section class="cover cover--charcoal" aria-label="Castellan Stockings box cover, charcoal">
    <svg class="cover__art" viewBox="0 0 320 468" aria-hidden="false">
      <defs>
        <linearGradient id="charcoal-pattern" x1="0" y1="0" x2="0.4" y2="1">
          <stop class="pattern-stop-a" offset="0"/>
          <stop class="pattern-stop-b" offset="1"/>
        </linearGradient>
      </defs>
      <path role="img" aria-label="Decorative concentric circle pattern along the left edge"
            d="M0 0 H98 C58 120 28 250 42 468 H0 Z" fill="url(#charcoal-pattern)"/>
      <path class="swoosh" d="M98 0 C58 120 28 250 42 468 L56 468 C44 260 76 120 106 0 Z"/>
    </svg>
    <div class="brand">
      <span class="brand__name">CASTELLAN</span>
      <span class="brand__line">STOCKINGS</span>
    </div>
  </section>

  <section class="cover cover--cocoa" aria-label="Castellan Stockings box cover, cocoa brown">
    <svg class="cover__art" viewBox="0 0 320 468" aria-hidden="false">
      <defs>
        <linearGradient id="cocoa-pattern" x1="0" y1="0" x2="0.4" y2="1">
          <stop class="pattern-stop-a" offset="0"/>
          <stop class="pattern-stop-b" offset="1"/>
        </linearGradient>
      </defs>
      <path role="img" aria-label="Decorative swirl and circle pattern along the left edge"
            d="M0 0 H98 C58 120 28 250 42 468 H0 Z" fill="url(#cocoa-pattern)"/>
      <path class="swoosh" d="M98 0 C58 120 28 250 42 468 L56 468 C44 260 76 120 106 0 Z"/>
    </svg>
    <div class="brand">
      <span class="brand__name">CASTELLAN</span>
      <span class="brand__line">STOCKINGS</span>
    </div>
  </section>

</main>
</body>
</html>
```